Bluewater Getaways KT needs a new Website

We have an old website that is just that - old. We need a fresh website that is professional graphic designed that has the following features.
1. Can be updated by ourselves in some areas.
2. Has a shopping cart.
3. Has links to download PDF files
4. Has links to other pages in the website
5. Includes social media links
6. Has a client log-in area
Full details in brief provided.

SORRY BUT IT'S URGENT. We've taken too long to write the details and it is now urgent. So my apologies I will be asking for designers to work quickly.

We will continue to use our existing web hosting company and url. Their is a link to the old website in the Design Brief.
Updates

UPDATE:  Please see the new file UPDATE TO DESIGN BRIEF.
Thanks for all your submissions to date.  We hope the update will assist with your designs.
As indicated in previous messages, we are happy with the Home Page + 1 Page in order to select the designer to work with in creating the full design. 

Thankyou Designers.  Much appreciate your efforts.
It's getting late here on Norfolk so I won't have much chance too review any more designs this evening.
But for your information:
Designer 7318405 Ravindra Mehta is so far the closest to what we are seeking.
Thanks again. 

Reason: Have extended to Monday 7 October to give time for designers to submit after feedback today. Especially given the time differences

Target Market(s)

Very wide audience. Current client group not that tech savvy, but we hope to broaden our market and sell more creative products, and so website needs to consider how people now use media, ie tablets & iphones.

Industry/Entity Type

Shopping

Requirements
Nice to have
• PLEASE SEE THE "UPDATE TO THE DESIGN BRIEF"

```html
<!DOCTYPE html>
<html lang="en">
<head>
<meta charset="utf-8">
<title>Bluewater Getaways KT – Home</title>
<link rel="stylesheet" href="https://fonts.googleapis.com/css2?family=Roboto+Condensed:wght@400;700&family=Oswald:wght@400&display=swap">
<style>
:root{
  --orange:#f7931e;
  --ink:#3a2418;
  --header-dark:#1f1f1f;
  --panel:#ffffff;
  --rule:#d6d6d6;
  --nav-top:#ffffff;
  --nav-bottom:#ececec;
  --sea-1:#0a6f8f;
  --sea-2:#17a8bd;
  --sea-3:#6fd1d4;
  --muted:#6b6b6b;
}
*{box-sizing:border-box;margin:0;padding:0}
html,body{width:1200px;height:882px;overflow:hidden}
body{position:relative;font-family:"Roboto Condensed",Arial,sans-serif;color:var(--ink);background:var(--sea-2)}
.backdrop{position:absolute;left:0;top:117px;width:1200px;height:765px;
  background:linear-gradient(180deg,var(--sea-1) 0%,var(--sea-2) 35%,var(--sea-3) 70%,#9fdcd3 100%)}
.site-header{position:absolute;left:0;top:0;width:1200px;height:117px;
  background:linear-gradient(180deg,#3a3a3a,var(--header-dark))}
.brand{position:absolute;left:20px;top:0;width:300px;height:117px;background:var(--panel);
  display:flex;align-items:center;justify-content:center;border-bottom:3px solid var(--orange)}
.brand-name{font-size:24px;font-weight:400;color:var(--ink)}
.tagline{position:absolute;left:377px;top:42px;font-family:"Oswald",sans-serif;font-size:31px;color:#fff;letter-spacing:.3px}
.tab{position:absolute;top:0;width:46px;height:64px;background:var(--orange);
  clip-path:polygon(0 0,100% 0,100% 100%,0 92%);display:flex;align-items:center;justify-content:center}
.tab.cart{left:931px}.tab.phone{left:987px}
.hotline{position:absolute;left:1042px;top:14px;font-family:"Oswald",sans-serif;font-size:25px;color:#fff;letter-spacing:1px}

.main-nav{position:absolute;left:20px;top:117px;width:300px;background:var(--panel);border-bottom:3px solid var(--orange)}
.main-nav a{display:block;height:42px;line-height:42px;padding-left:20px;font-size:15px;color:var(--orange);text-decoration:none;
  background:linear-gradient(180deg,var(--nav-top),var(--nav-bottom));border-bottom:1px dashed var(--rule)}
.main-nav a:last-child{border-bottom:none}

.news{position:absolute;left:20px;top:668px;width:300px;height:214px;background:var(--panel);padding:24px 10px 0 10px;overflow:hidden}
.news h2{font-weight:400;font-size:20px;margin-bottom:8px;color:#2b1d14}
.news-item{padding:0 18px 8px 2px;border-bottom:1px dashed var(--rule);margin-bottom:8px;font-size:13px;line-height:20px}
.news-item h3{font-size:13px;font-weight:700;color:var(--orange);text-transform:uppercase}
.news-item .meta{color:var(--muted);font-size:12.5px}
.scroll-track{position:absolute;left:304px;top:732px;width:6px;height:150px;background:#eee}
.scroll-thumb{position:absolute;left:304px;top:742px;width:6px;height:55px;background:var(--orange);border-radius:3px}

.content{position:absolute;left:330px;top:128px;width:540px;height:754px;background:var(--panel);padding:10px}
.slider{position:relative;width:520px;height:385px;background:linear-gradient(180deg,#5fa4dc 0%,#9cc6e6 40%,#a78a68 60%,#7a5b3e 100%)}
.slider .arrow{position:absolute;top:167px;width:36px;height:70px;background:rgba(0,0,0,.25);display:flex;align-items:center;justify-content:center}
.slider .prev{left:0}.slider .next{right:0}
.slider .caption{position:absolute;left:0;bottom:0;width:520px;height:68px;background:rgba(40,40,40,.6);color:#fff;font-size:12px;line-height:20px;padding:9px 12px}
.content h1{font-weight:400;font-size:30px;margin:22px 0 9px;color:#2b1d14}
.content p{font-size:12px;line-height:20px;margin-bottom:20px}
.content p a{color:var(--orange);text-decoration:none}
.content hr{border:none;border-top:1px dashed var(--rule);margin-top:16px}

.sidebar{position:absolute;left:880px;top:128px;width:300px;height:754px;background:var(--panel);padding:10px}
.card{position:relative;border:1px dashed #cfcfcf;background:linear-gradient(180deg,#fff 60%,#f1f1f1);padding:8px 10px;margin-bottom:11px}
.card h2{font-weight:400;font-size:20px;color:#2b1d14;margin-bottom:4px}
.card .lines{font-size:12px;line-height:15px}
.card.location,.card.telephone,.card.links{height:123px}
.card.links .lines{line-height:20px}
.card .icon{position:absolute}
.map-art{right:10px;top:30px;width:100px;height:76px;background:linear-gradient(180deg,#3a3a3a,#8a8a8a);border-radius:4px}
.gallery{display:grid;grid-template-columns:125px 125px;gap:10px;margin-top:8px}
.thumb{height:122px;display:flex;align-items:center;justify-content:center}
.thumb.a{background:linear-gradient(180deg,#8fa6b4,#6a6f6a)}
.thumb.b{background:linear-gradient(180deg,#b7b39a,#5c5447)}
.thumb.c{background:linear-gradient(180deg,#7a8a72,#6f5c4a)}
.thumb.d{background:linear-gradient(180deg,#8fb3d4,#8a7258)}
.view-all{display:inline-block;margin-top:11px;background:var(--orange);color:#fff;font-size:15px;padding:3px 10px;text-decoration:none}
</style>
</head>
<body>
<div class="backdrop" role="img" aria-label="Turquoise tropical lagoon with sandy shoreline"></div>

<header class="site-header">
  <div class="brand"><span class="brand-name">Bluewater Getaways KT</span></div>
  <div class="tagline">“GETAWAYS MADE FOR EVERYONE!”</div>
  <a class="tab cart" aria-label="Shopping cart">
    <svg width="26" height="24" viewBox="0 0 26 24"><path d="M1 3h4l3 12h13l3-9H7" fill="none" stroke="#222" stroke-width="2.5" stroke-linejoin="round"/><circle cx="10" cy="20" r="2.2" fill="#222"/><circle cx="19" cy="20" r="2.2" fill="#222"/></svg>
  </a>
  <a class="tab phone" aria-label="Call us">
    <svg width="22" height="24" viewBox="0 0 22 24"><path d="M5 1l4 5-2.5 3c1.5 3.5 4 6 7.5 7.5L17 14l5 4-2 4C11 22 1 12 1 3z" fill="#222"/></svg>
  </a>
  <div class="hotline">1800 555 013</div>
</header>

<nav class="main-nav">
  <a href="#">Home</a><a href="#">Governance</a><a href="#">Norfolk Island</a><a href="#">Our Mission &amp; Values</a>
  <a href="#">Services</a><a href="#">Our Facilitators</a><a href="#">Our Shop</a><a href="#">Holiday Programs</a>
  <a href="#">Design your own Norfolk Island Holiday</a><a href="#">KreativeWorks Projects</a>
  <a href="#">Schoolies, Siblings&amp; Family Holidays</a><a href="#">Make a Booking</a><a href="#">Testimonials</a>
</nav>

<aside class="news">
  <h2>Latest News</h2>
  <div class="news-item">
    <h3>Rockhampton Coast Rail Weekend</h3>
    <div>$790 Ask for details - departures anytime</div>
    <div class="meta">NEW HOLIDAY</div>
    <div class="meta">13 October 2013</div>
  </div>
  <div class="news-item">
    <h3>Thailand for 8 days in early February 2013</h3>
    <div>Contact us for itinerary - several guests confirmed, seeking more travel companions. 8 days $3,990 all</div>
  </div>
</aside>
<div class="scroll-track"></div><div class="scroll-thumb"></div>

<main class="content">
  <div class="slider" role="img" aria-label="Holiday guests in helmets riding camels along a sunny beach">
    <span class="arrow prev"><svg width="12" height="20" viewBox="0 0 12 20"><path d="M10 2L2 10l8 8" fill="none" stroke="#fff" stroke-width="2"/></svg></span>
    <span class="arrow next"><svg width="12" height="20" viewBox="0 0 12 20"><path d="M2 2l8 8-8 8" fill="none" stroke="#fff" stroke-width="2"/></svg></span>
    <div class="caption">Bluewater Getaways KT is a private company offering quality supported holidays and travel options for adults with intellectual disabilities or acquired brain injury. We are based in Coral Heads on Queensland’s Sunshine Coast</div>
  </div>
  <h1>Welcome to our site</h1>
  <p>Bluewater Getaways KT is a private company offering quality supported holidays and travel options for adults with intellectual disabilities or acquired brain injury. We are based in Coral Heads on Queensland’s Sunshine Coast.&nbsp; We began our operation in 2001 as Coastal Supported Holidays and now conduct holiday programs throughout Australia and Overseas.</p>
  <p>As a private service provider we do not access funding of any kind, be it donations or grants, and our service is essentially a user-pays system. We base our operation and quality framework on the standards set by the Australian Federal and State Government Disability Departments.</p>
  <p>Whilst we are experienced recreation/tourism facilitators we consider ourselves first and foremost as Disability Service Providers.&nbsp; We take seriously our commitment to supporting adults in their quest for community inclusion and access to quality recreation.&nbsp; <a href="#">Read more</a></p>
  <hr>
</main>

<aside class="sidebar">
  <section class="card location">
    <h2>Location&amp; Contacts</h2>
    <div class="lines">Harbour Lane, Kingfisher Town<br>PO Box 512<br>Norfolk Island NSW 2900<br>SOUTH PACIFIC<br>N.B.N. 471 206 558</div>
    <div class="icon map-art" role="img" aria-label="World map"></div>
  </section>
  <section class="card telephone">
    <h2>Telephone</h2>
    <div class="lines">International + 67 23 55019<br>Australia 1800 555 013<br>New Zealand</div>
    <svg class="icon" style="right:40px;top:32px" width="36" height="40" viewBox="0 0 22 24"><path d="M5 1l4 5-2.5 3c1.5 3.5 4 6 7.5 7.5L17 14l5 4-2 4C11 22 1 12 1 3z" fill="#111"/></svg>
  </section>
  <section class="card links">
    <h2>Email, Website &amp; Social</h2>
    <div class="lines">hello@bluewatergetaways.org<br>www.bluewatergetaways.org<br>social.example/bluewater</div>
    <svg class="icon" style="right:22px;top:48px" width="66" height="32" viewBox="0 0 66 32"><rect x="2" y="6" width="27" height="18" fill="#fff" stroke="#111" stroke-width="2"/><path d="M2 6l13.5 10L29 6" fill="none" stroke="#111" stroke-width="2"/><circle cx="49" cy="15" r="14" fill="#fff" stroke="#111" stroke-width="2"/><path d="M35 15h28M49 1v28" fill="none" stroke="#111" stroke-width="1.5"/></svg>
  </section>
  <section class="card">
    <h2>Images &amp; Video</h2>
    <div class="gallery">
      <div class="thumb a" role="img" aria-label="Group photo of guests on holiday"><svg width="50" height="36" viewBox="0 0 50 36"><rect x="1" y="1" width="48" height="34" fill="none" stroke="#fff" stroke-width="2"/><path d="M5 31l13-14 9 9 7-6 11 11z" fill="#fff"/><circle cx="36" cy="10" r="3" fill="#fff"/></svg></div>
      <div class="thumb b" role="img" aria-label="Video of a horse-drawn carriage ride"><svg width="36" height="36" viewBox="0 0 36 36"><circle cx="18" cy="18" r="17" fill="rgba(255,255,255,.7)"/><path d="M14 10l12 8-12 8z" fill="#555"/></svg></div>
      <div class="thumb c" role="img" aria-label="Video of a guest feeding a kangaroo"><svg width="36" height="36" viewBox="0 0 36 36"><circle cx="18" cy="18" r="17" fill="rgba(255,255,255,.7)"/><path d="M14 10l12 8-12 8z" fill="#555"/></svg></div>
      <div class="thumb d" role="img" aria-label="Guests riding camels on the beach"><svg width="50" height="36" viewBox="0 0 50 36"><rect x="1" y="1" width="48" height="34" fill="none" stroke="#fff" stroke-width="2"/><path d="M5 31l13-14 9 9 7-6 11 11z" fill="#fff"/><circle cx="36" cy="10" r="3" fill="#fff"/></svg></div>
    </div>
    <a class="view-all" href="#">View All</a>
  </section>
</aside>
</body>
</html>
```